New Zealand Luggage Importer Needs Business Cards

We need professional, creative and fashionable business cards created.
We are based in New Zealand and import and distribute high-end, quality, fashionable and durable luggage.
We pride ourselves on selling the very best quality luggage, second only to 1 brand (which we won't mention here)...we use the same manufacturer. However, our prices are much more reasonable.
Industry/Entity Type
Business
Contact Information for Business Card
Mark Dunsley
027 512 4068
3/17 Harlow Street, Pinecrest Flats, Auckland, 0614
PO Box 204377, Fernside, Auckland 0731
09-528-3916
sales@brivancases.co.nz / www.brivancases.co.nz

```html
<!DOCTYPE html>
<html lang="en">
<head>
<meta charset="utf-8">
<title>Brivan Cases – Business Card</title>
<link rel="stylesheet" href="https://fonts.googleapis.com/css2?family=Raleway:wght@300;400&display=swap">
<style>
  :root {
    --page: #ffffff;
    --card-black: #080808;
    --band-black: #050505;
    --quilt-light: #2a2a2c;
    --quilt-dark: #0b0b0c;
    --gold: #d2ae68;
    --gold-soft: #c9a35a;
    --white: #f4f4f4;
    --silver-a: #5c5c5c;
    --silver-b: #bdbdbd;
    --frame: #5a5a5a;
  }
  html, body {
    margin: 0;
    padding: 0;
    width: 1200px;
    height: 1200px;
    overflow: hidden;
    background: var(--page);
    font-family: "Raleway", "Helvetica Neue", Arial, sans-serif;
  }
  .canvas { position: relative; width: 1200px; height: 1200px; }

  .card {
    position: absolute;
    left: 181px;
    width: 838px;
    height: 466px;
    background: var(--card-black);
    overflow: hidden;
  }
  .card--front { top: 102px; }
  .card--back { top: 598px; }

  .quilt {
    position: absolute;
    left: 0; top: 0; width: 100%; height: 100%;
    background:
      radial-gradient(ellipse 70% 45% at 50% 0%, var(--quilt-light) 0%, rgba(20,20,22,0.6) 45%, rgba(8,8,8,0) 80%),
      linear-gradient(180deg, #151516 0%, var(--quilt-dark) 70%, #070707 100%);
  }

  .rule {
    position: absolute;
    left: 0; width: 100%; height: 2px;
    background: linear-gradient(90deg, var(--silver-a), var(--silver-b) 50%, var(--silver-a));
  }
  .band {
    position: absolute;
    left: 0; width: 100%;
    background: var(--band-black);
  }

  /* front */
  .person-name {
    position: absolute;
    left: 45px; top: 250px;
    margin: 0;
    font-weight: 300;
    font-size: 38px;
    letter-spacing: 0.5px;
    color: var(--white);
    line-height: 1;
  }
  .person-name .first { color: var(--gold); }

  .contact {
    position: absolute;
    display: flex;
    align-items: center;
    gap: 10px;
    font-size: 12.5px;
    font-weight: 400;
    color: var(--gold);
    letter-spacing: 0.2px;
    text-transform: uppercase;
    line-height: 15px;
  }
  .contact svg { flex: none; }
  .contact--email { left: 51px; top: 354px; }
  .contact--web { left: 365px; top: 353px; }
  .contact--phone { left: 659px; top: 348px; gap: 20px; }
  .contact--address { left: 234px; top: 421px; }

  /* back */
  .brand-frame {
    position: absolute;
    left: 74px; top: 177px;
    width: 689px; height: 113px;
    border: 1px solid var(--frame);
    background: #030303;
    display: flex;
    align-items: center;
    justify-content: center;
  }
  .brand-name {
    margin: 0;
    font-weight: 300;
    font-size: 58px;
    letter-spacing: 6px;
    color: var(--gold);
    text-transform: uppercase;
  }
  .back-url {
    position: absolute;
    left: 0; width: 100%;
    top: 331px;
    text-align: center;
    font-size: 17px;
    font-weight: 400;
    color: var(--white);
    text-transform: uppercase;
  }
</style>
</head>
<body>
<div class="canvas">

  <section class="card card--front">
    <div class="quilt" role="img" aria-label="Black quilted leather upholstery texture"></div>

    <h1 class="person-name"><span class="first">MARK</span> DUNSLEY</h1>

    <div class="rule" style="top:322px"></div>
    <div class="band" style="top:324px; height:78px"></div>
    <div class="rule" style="top:402px"></div>

    <div class="contact contact--email">
      <svg width="24" height="17" viewBox="0 0 24 17" aria-hidden="true">
        <rect x="0" y="0" width="24" height="17" fill="#fff"/>
        <path d="M0 0 L12 9 L24 0" fill="none" stroke="#050505" stroke-width="1.8"/>
        <path d="M0 17 L9 7.5 M24 17 L15 7.5" stroke="#050505" stroke-width="1.4"/>
      </svg>
      <span>sales@brivancases.co.nz</span>
    </div>

    <div class="contact contact--web">
      <svg width="25" height="25" viewBox="0 0 25 25" aria-hidden="true">
        <circle cx="12.5" cy="12.5" r="11.5" fill="#fff"/>
        <path d="M4 8 Q9 6 11 10 T8 17 M14 3 Q16 8 21 8 M13 22 Q15 15 21 16" fill="none" stroke="#050505" stroke-width="2"/>
      </svg>
      <span>www.brivancases.co.nz</span>
    </div>

    <div class="contact contact--phone">
      <svg width="24" height="24" viewBox="0 0 24 24" aria-hidden="true">
        <path fill="#fff" d="M6.6 10.8c1.4 2.8 3.8 5.1 6.6 6.6l2.2-2.2c.3-.3.7-.4 1-.2 1.1.4 2.3.6 3.6.6.6 0 1 .4 1 1V20c0 .6-.4 1-1 1C10.6 21 3 13.4 3 4c0-.6.4-1 1-1h3.5c.6 0 1 .4 1 1 0 1.3.2 2.5.6 3.6.1.3 0 .7-.2 1L6.6 10.8z"/>
      </svg>
      <span>027 512 4068<br>09-528-3916</span>
    </div>

    <div class="contact contact--address">
      <svg width="18" height="26" viewBox="0 0 18 26" aria-hidden="true">
        <path fill="#fff" d="M9 0C4 0 0 4 0 9c0 6.5 9 17 9 17s9-10.5 9-17c0-5-4-9-9-9zm0 12.5A3.5 3.5 0 1 1 9 5.5a3.5 3.5 0 0 1 0 7z"/>
      </svg>
      <span>3/17 Harlow Street, Pinecrest Flats, Auckland, 0614<br>PO Box 204377, Fernside, Auckland 0731</span>
    </div>
  </section>

  <section class="card card--back">
    <div class="quilt" role="img" aria-label="Black quilted leather upholstery texture"></div>

    <div class="rule" style="top:151px"></div>
    <div class="band" style="top:153px; height:158px"></div>
    <div class="rule" style="top:311px"></div>

    <div class="brand-frame">
      <p class="brand-name">Brivan Cases</p>
    </div>

    <div class="back-url">www.brivancases.co.nz</div>
  </section>

</div>
</body>
</html>
```